oKRAL Letterhead

We need a letterhead design for a newly built company called OKRAL Prime Radiology Systems Inc. We supply healthcare products specifically imaging solutions to hospitals and medical clinics. We are an exclusive distributor of Brightholm Health products. We prefer royal; blue to be used for the design. we prefer that OKRAL will be read as KRAL, maybe writing it as oKRAL will be appropriate and highlighted in the design.

Target Market(s)

Hospitals and healthcare professionals

Industry/Entity Type

Healthcare

Font styles to use
Sans Serif

Colors
0593ce
0f5aa6

Requirements
Must have
• Logo should emphasize Kral Prime Radiology Systems Inc Instead of Okral but still spelled as Okral Prime Radiology Systems Inc since this is the registered business name.

```html
<!DOCTYPE html>
<html lang="en">
<head>
<meta charset="utf-8">
<title>oKRAL Letterhead and Folder</title>
<link rel="stylesheet" href="https://fonts.googleapis.com/css2?family=Roboto:wght@700&family=Roboto+Condensed:wght@500&family=Questrial&display=swap">
<style>
  :root {
    --backdrop: #ececec;
    --paper: #ffffff;
    --royal: #0f5aa6;
    --sky: #0593ce;
    --folder: #1f5592;
    --ink-grey: #5a5a5a;
    --tagline-light: #e6ecf3;
  }
  * { margin: 0; padding: 0; box-sizing: border-box; }
  html, body { width: 1200px; height: 815px; overflow: hidden; }
  body { background: var(--backdrop); position: relative; font-family: "Roboto", Arial, sans-serif; }

  .letterhead {
    position: absolute; left: 80px; top: 72px; width: 482px; height: 682px;
    background: var(--paper); overflow: hidden;
  }
  .brand { position: absolute; }
  .brand-name {
    font-family: "Roboto", Arial, sans-serif; font-weight: 700;
    letter-spacing: -0.5px; line-height: 1;
  }
  .brand-tagline {
    font-family: "Roboto Condensed", "Arial Narrow", sans-serif; font-weight: 500;
    text-transform: uppercase; white-space: nowrap; line-height: 1;
  }
  .letterhead .brand { left: 46px; top: 42px; }
  .letterhead .brand-name { font-size: 31px; color: var(--royal); }
  .letterhead .brand-tagline { font-size: 8.6px; color: var(--royal); margin-top: 3px; letter-spacing: 0.1px; }

  .contact {
    position: absolute; left: 356px; top: 42px;
    font-family: "Questrial", "Century Gothic", sans-serif; font-size: 6.6px; color: var(--ink-grey);
    line-height: 9px; list-style: none;
  }
  .contact-address { margin-bottom: 6px; }
  .contact-line { display: flex; align-items: center; gap: 5px; height: 10px; }
  .contact-icon { width: 7px; height: 7px; flex: none; }

  .wave { position: absolute; left: 0; bottom: 0; width: 482px; height: 44px; }

  .folder {
    position: absolute; left: 638px; top: 70px; width: 483px; height: 685px;
    background: var(--folder);
  }
  .folder .brand { left: 134px; top: 96px; }
  .folder .brand-name { font-size: 58px; color: #ffffff; letter-spacing: -1px; }
  .folder .brand-tagline { font-size: 13.6px; color: var(--tagline-light); margin-top: 5px; letter-spacing: 0.2px; }
</style>
</head>
<body>

<section class="letterhead" aria-label="Letterhead">
  <div class="brand">
    <div class="brand-name">oKRAL</div>
    <div class="brand-tagline">Prime Radiology Systems Inc</div>
  </div>

  <address class="contact">
    <div class="contact-address">4th Floor, 58 Harlow Lane<br>London, UK, N7 4QP</div>
    <div class="contact-line">
      <svg class="contact-icon" viewBox="0 0 7 7"><rect width="7" height="7" rx="1.2" fill="#0f5aa6"/><path d="M2 1.6 L2.9 1.6 L3.1 2.6 L2.6 3 Q3 4 4 4.4 L4.4 3.9 L5.4 4.1 L5.4 5 Q3.8 5.2 2.8 4.2 Q1.8 3.2 2 1.6Z" fill="#fff"/></svg>
      <span>+44 (0)2074 5512</span>
    </div>
    <div class="contact-line">
      <svg class="contact-icon" viewBox="0 0 7 7"><rect width="7" height="7" rx="1.2" fill="#0f5aa6"/><rect x="1.6" y="2.6" width="3.8" height="2.6" fill="#fff"/><rect x="2.4" y="1.4" width="2.2" height="1.4" fill="#fff"/></svg>
      <span>+44 (0)2074 5530</span>
    </div>
    <div class="contact-line">
      <svg class="contact-icon" viewBox="0 0 7 7"><rect width="7" height="7" rx="1.2" fill="#0f5aa6"/><rect x="1.4" y="2" width="4.2" height="3" fill="#fff"/><path d="M1.4 2 L3.5 3.6 L5.6 2" stroke="#0f5aa6" stroke-width="0.5" fill="none"/></svg>
      <span>info@okral-prs.com</span>
    </div>
    <div class="contact-line">
      <svg class="contact-icon" viewBox="0 0 7 7"><rect width="7" height="7" rx="1.2" fill="#0f5aa6"/><circle cx="3.5" cy="3.5" r="2" fill="none" stroke="#fff" stroke-width="0.6"/><path d="M1.5 3.5 H5.5 M3.5 1.5 V5.5" stroke="#fff" stroke-width="0.4"/></svg>
      <span>www.okral-prs.com</span>
    </div>
  </address>

  <svg class="wave" viewBox="0 0 482 44" preserveAspectRatio="none" aria-hidden="true">
    <defs>
      <linearGradient id="waveDeep" x1="0" y1="0" x2="1" y2="0">
        <stop offset="0" stop-color="#0f5aa6"/>
        <stop offset="0.5" stop-color="#0593ce"/>
        <stop offset="1" stop-color="#0f5aa6"/>
      </linearGradient>
      <linearGradient id="waveLight" x1="0" y1="0" x2="1" y2="0">
        <stop offset="0" stop-color="#0593ce"/>
        <stop offset="1" stop-color="#4fb0dd"/>
      </linearGradient>
    </defs>
    <path d="M0 6 C120 -2 260 -2 482 10 L482 44 L0 44 Z" fill="url(#waveLight)"/>
    <path d="M0 12 C140 4 300 4 482 22 L482 44 L0 44 Z" fill="#d9e4ef"/>
    <path d="M0 20 C150 10 310 14 482 30 L482 44 L0 44 Z" fill="url(#waveDeep)"/>
  </svg>
</section>

<section class="folder" aria-label="Presentation folder cover">
  <div class="brand">
    <div class="brand-name">oKRAL</div>
    <div class="brand-tagline">Prime Radiology Systems Inc</div>
  </div>
</section>

</body>
</html>
```